Business Card Design

we are a wellness center offering therapeutic massage modalities and yoga and meditation classes. I would like to see designs that incorporate the colors of my current logo (image uploaded) BUT I would like to change my logo slightly so that the three words wrapping around my image are: massage yoga wellness (in other words, take out skin).

Industry/Entity Type

Massage

Contact Information for Business Card

Lena R. Calloway, BS, CMT, E-RYT, Owner
427 E. Brindle Ave., Suite 3C
Hampton, VA 23581
757-302-5594 (office)
757-861-2047 (cell)
fernleafrestorative.example
fernleafrestorative@mailbox.example

Requirements
Nice to have
• I'd like to have my logo as a watermark on the back side, but if that's not doable, no big deal. Thanks.

```html
<!DOCTYPE html>
<html lang="en">
<head>
<meta charset="utf-8">
<title>Fernleaf Restorative – Business Card</title>
<link rel="stylesheet" href="https://fonts.googleapis.com/css2?family=Montserrat:wght@400;500&display=swap">
<style>
  :root {
    --canvas: #ffffff;
    --frame: #5dd6f0;
    --band: #4dd8f8;
    --sage: #93d4c3;
    --sage-soft: #b7e3d7;
    --coral: #d9574a;
    --dot: #e8141b;
    --ink: #111111;
  }
  * { margin: 0; padding: 0; box-sizing: border-box; }
  html, body {
    width: 988px; height: 1200px; overflow: hidden;
    background: var(--canvas);
    font-family: "Montserrat", sans-serif;
    color: var(--ink);
  }
  .sheet { position: relative; width: 988px; height: 1200px; }
  .card {
    position: absolute; left: 22px; width: 926px; height: 538px;
    border: 3px solid var(--frame); border-radius: 40px;
    overflow: hidden; background: var(--canvas);
  }
  .card--front { top: 22px; }
  .card--back { top: 620px; }
  .card__art { position: absolute; left: 0; top: 0; }
  .abs { position: absolute; white-space: nowrap; line-height: 1; }

  .holder-name { left: 86px; top: 89px; font-size: 41px; font-weight: 400; letter-spacing: 0.5px; }
  .holder-creds { left: 0; width: 552px; text-align: center; top: 135px; font-size: 22px; letter-spacing: 0.5px; }
  .holder-role { left: 0; width: 540px; text-align: center; top: 164px; font-size: 30px; }
  .address { left: 86px; top: 263px; font-size: 24px; line-height: 34px; white-space: nowrap; }
  .contact { left: 94px; top: 367px; font-size: 19px; line-height: 29px; }
  .contact--email { top: 424px; }
  .band { position: absolute; left: 37px; top: 463px; width: 679px; height: 14px; background: var(--band); }
  .url { left: 98px; top: 484px; font-size: 23px; letter-spacing: 0.3px; }

  .brand-name {
    left: 230px; width: 690px; text-align: center; top: 168px;
    font-size: 58px; font-weight: 500; color: var(--coral); letter-spacing: 0.5px;
  }
  .services {
    left: 230px; width: 690px; top: 326px;
    display: flex; justify-content: center; align-items: center; gap: 12px;
    font-size: 24px; letter-spacing: 0.4px;
  }
  .services__dot { width: 22px; height: 22px; border-radius: 50%; background: var(--dot); }
</style>
</head>
<body>
<main class="sheet">

  <section class="card card--front" aria-label="Card front">
    <svg class="card__art" width="926" height="538" viewBox="0 0 926 538" aria-hidden="true">
      <path d="M572 163 C 650 330, 760 500, 926 520" fill="none" stroke="var(--frame)" stroke-width="3"/>
    </svg>
    <svg class="card__art" width="926" height="538" viewBox="0 0 926 538" role="img" aria-label="Decorative emblem area">
      <defs>
        <radialGradient id="emblemFill" cx="0.4" cy="0.5" r="0.6">
          <stop offset="0" stop-color="var(--sage-soft)"/>
          <stop offset="1" stop-color="var(--sage)"/>
        </radialGradient>
      </defs>
      <circle cx="905" cy="295" r="196" fill="url(#emblemFill)"/>
    </svg>

    <div class="abs holder-name">Lena R. Calloway</div>
    <div class="abs holder-creds">BS, CMT, E-RYT</div>
    <div class="abs holder-role">Owner</div>

    <div class="abs address">427 E. Brindle Ave.,<br>Suite 3C Hampton, VA 23581</div>

    <div class="abs contact">Phone : 757-302-5594 (office)<br>Phone : 757-861-2047 (cell)</div>
    <div class="abs contact contact--email">E-mail : fernleafrestorative@mailbox.example</div>

    <div class="band"></div>
    <div class="abs url">URL : fernleafrestorative.example</div>
  </section>

  <section class="card card--back" aria-label="Card back">
    <svg class="card__art" width="926" height="538" viewBox="0 0 926 538" role="img" aria-label="Decorative foliage area">
      <defs>
        <linearGradient id="foliageFill" x1="0" y1="0" x2="1" y2="1">
          <stop offset="0" stop-color="var(--sage)"/>
          <stop offset="1" stop-color="var(--sage-soft)"/>
        </linearGradient>
      </defs>
      <path d="M0 60 C 80 90, 180 110, 215 150 C 220 260, 180 380, 60 485 L 0 485 Z" fill="url(#foliageFill)"/>
    </svg>

    <div class="abs brand-name">Fernleaf Restorative</div>
    <div class="abs services">
      <span>Massage</span><span class="services__dot"></span>
      <span>Yoga</span><span class="services__dot"></span>
      <span>Wellness</span>
    </div>
  </section>

</main>
</body>
</html>
```